Brightmoor Partners Branding Revamp

We are a consulting company, looking for a way to display and promote our brand. We have 2 sides to the business- Brightmoor (financial) and Partners (cyber security). The financial side products relate to business necessities: card processing, website design/hosting/maintenance, VoIP phone systems. The cyber security side promotes a bundled package of 4 solutions: network vulnerability scan, dark web scan, anti-ransomeware/malware software, and image-level backups. We want people to understand that partnering with Brightmoor Partners gives them “Elevated Peace of Mind” (tagline). Current badge and logos uploaded.

Target Market(s)

Small businesses

Contact Information for Business Card

Lena Marwick, Vice President, lena@brightmoorpartners.example, 555-806-1937, www.brightmoorpartners.example

Requirements
Nice to have
• I do prefer the darker background for front and back

```html
<!DOCTYPE html>
<html lang="en">
<head>
<meta charset="utf-8">
<title>Brightmoor Partners – Business Card</title>
<link href="https://fonts.googleapis.com/css2?family=Michroma&family=Open+Sans:wght@400&display=swap" rel="stylesheet">
<style>
  :root {
    --page: #e9e9e9;
    --card-dark: #0d0d0d;
    --card-mid: #262626;
    --black: #000000;
    --red: #e21b25;
    --red-deep: #9c0c12;
    --white: #ececec;
  }
  html, body {
    margin: 0;
    width: 1200px;
    height: 1190px;
    overflow: hidden;
    background: var(--page);
  }
  .card {
    position: absolute;
    overflow: hidden;
    background: radial-gradient(ellipse at 25% 40%, var(--card-mid) 0%, var(--card-dark) 70%);
  }
  .card-front { left: 175px; top: 60px; width: 850px; height: 485px; }
  .card-back  { left: 168px; top: 632px; width: 850px; height: 486px; }

  .front-edge {
    position: absolute; right: 0; top: 0; width: 125px; height: 100%;
    background: var(--black);
  }
  .brand-mark {
    position: absolute; left: 395px; top: 170px; width: 60px; height: 60px;
    background: var(--red);
  }
  .brand-name {
    position: absolute; left: 0; width: 725px; text-align: center;
    font-family: "Michroma", sans-serif; color: var(--white); margin: 0;
  }
  .brand-name-main { top: 295px; font-size: 44px; letter-spacing: 6px; }
  .brand-name-sub  { top: 365px; font-size: 22px; letter-spacing: 26px; padding-left: 26px; }

  .back-edge {
    position: absolute; left: 0; top: 0; width: 123px; height: 100%;
    background: var(--black);
  }
  .back-brand {
    position: absolute; left: 40px; top: 175px; margin: 0;
    font-family: "Michroma", sans-serif; color: var(--red);
    font-size: 46px; line-height: 1.35; letter-spacing: 2px;
  }
  .holder {
    position: absolute; right: 25px; top: 40px; text-align: right;
  }
  .holder-name {
    margin: 0; font-family: "Michroma", sans-serif; color: var(--red);
    font-size: 25px; letter-spacing: 2px; line-height: 1.1;
  }
  .holder-role {
    margin: 4px 5px 0 0; font-family: "Open Sans", sans-serif; color: var(--white);
    font-size: 17px;
  }
  .contact-list {
    position: absolute; right: 25px; top: 360px; margin: 0; padding: 0; list-style: none;
  }
  .contact-item {
    display: flex; justify-content: flex-end; align-items: center; gap: 26px;
    height: 37px; font-family: "Open Sans", sans-serif; color: var(--white);
    font-size: 24px;
  }
  .contact-item svg { width: 24px; height: 24px; fill: var(--red); }
</style>
</head>
<body>
  <section class="card card-front">
    <div class="front-edge"></div>
    <div class="brand-mark"></div>
    <p class="brand-name brand-name-main">BRIGHTMOOR</p>
    <p class="brand-name brand-name-sub">PARTNERS</p>
  </section>

  <section class="card card-back">
    <div class="back-edge"></div>
    <p class="back-brand">BRIGHTMOOR<br>PARTNERS</p>
    <div class="holder">
      <p class="holder-name">LENA MARWICK</p>
      <p class="holder-role">Managing Member</p>
    </div>
    <ul class="contact-list">
      <li class="contact-item">555-806-1937
        <svg viewBox="0 0 24 24"><path d="M6 2l4 4-2 3c1 3 3 5 6 7l3-2 4 4-3 3C10 20 4 14 3 5z"/></svg>
      </li>
      <li class="contact-item">555-806-1938
        <svg viewBox="0 0 24 24"><path d="M7 2h10v7H7zM3 10h18v11H3zm4 4v4h10v-4z"/></svg>
      </li>
      <li class="contact-item">lena@brightmoorpartners.example
        <svg viewBox="0 0 24 24"><path d="M2 5h20v14H2zm2 2v1l8 6 8-6V7l-8 6z"/></svg>
      </li>
    </ul>
  </section>
</body>
</html>
```